Lumokrit alias Jarek hat fantastische Arbeit geleistet. Zeitnahe Kommunikation, zeitnahe Umsetzung des Feedbacks und zeitnahe Bereitstellung des fertigen Projektes. Gerne jederzeit wieder.
Zielgruppe
Onlinemarketing Services für kleine und mittlere Unternehmen, wie z.B. Webseitenbau, Social Media Kampagnen oder Suchmaschinenoptimierung. Zu unseren Kunden gehören Handwerker, Tierärzte, Rechtsanwälte oder Kfz-Meisterbetriebe. Wir bedienen 6.000 Branchen von Aalräucherei bis Zylinderschleiferei, fokussieren uns aber stark auf das Handwerk.
Aufgabenstellung
Wir planen unsere Produkte unseren Kunden auf einer Plattform zur Verfügung zustellen. Hier sollen sie sich einloggen können und die Self und Managed Services nutzen können. Wir benötigen dafür eine Visualisierung. Also keine echte Webseite, sondern eine Anmutung. Sie soll nicht klickbar sein, aber sich schon wie eine fertige Webseite anfühlen.
Insgesamt sollen 3 Unterseiten gestaltet werden, die wir bereits skizziert (siehe Mockups) haben. Wir sind offen für deine Gestaltungsideen, Hauptsache es sieht nach was aus. Uns ist zudem wichtig, dass du dich bei der Farbgestaltung an der Webseite www.falvoria.com orientierst (Faust-Icon, Logo und Farbe).

```html
<!DOCTYPE html>
<html lang="de">
<head>
<meta charset="utf-8">
<title>falvoria.com – Marketing und Recruiting</title>
<link rel="stylesheet" href="https://fonts.googleapis.com/css2?family=Manrope:wght@400;500;600;700;800&display=swap">
<style>
  :root{
    --orange:#f28705;
    --peach:#fde6d4;
    --apricot:#fdb86a;
    --cyan:#74e3e8;
    --red:#e85555;
    --ink:#1b1b22;
    --purple:#9a3cf0;
    --footer:#101420;
    --white:#ffffff;
  }
  *{margin:0;padding:0;box-sizing:border-box}
  html,body{width:876px;height:1200px;overflow:hidden}
  body{position:relative;background:var(--white);font-family:'Manrope',sans-serif;color:var(--ink)}
  .abs{position:absolute}

  .blob{position:absolute;border-radius:50%}
  .blob--peach{left:499px;top:-110px;width:500px;height:500px;background:var(--peach)}
  .blob--apricot{left:452px;top:262px;width:46px;height:46px;background:var(--apricot)}
  .blob--cyan{left:634px;top:419px;width:44px;height:44px;background:var(--cyan)}

  .brand{left:26px;top:13px;display:flex;align-items:center;gap:7px}
  .brand__dot{width:31px;height:31px;border-radius:50%;background:var(--orange)}
  .brand__name{font-size:19px;font-weight:700;color:#4a4a4a}
  .nav{left:224px;top:23px;display:flex;gap:20px;font-size:12.5px;font-weight:500}
  .btn{display:flex;align-items:center;justify-content:center;background:var(--orange);color:var(--white);font-weight:600;border-radius:3px;box-shadow:0 2px 4px rgba(0,0,0,.12)}
  .btn--head{left:568px;top:16px;width:133px;height:28px;font-size:12px}
  .btn--ghost{left:719px;top:16px;width:133px;height:28px;font-size:12px;background:var(--white);color:var(--purple);border:1px solid var(--purple);box-shadow:none}

  .hero__photo{left:466px;top:173px;width:317px;height:207px;border-radius:9px;transform:rotate(-7deg);
    background:linear-gradient(135deg,#8a7a66 0%,#5e5a58 40%,#3f4a66 70%,#a35a38 100%)}
  .hero__title{left:100px;top:141px;font-size:37px;font-weight:800;line-height:30.5px;letter-spacing:2.6px}
  .hero__text{left:100px;top:274px;width:340px;font-size:10.5px;line-height:19.5px}
  .hero__text p+p{margin-top:19.5px}
  .btn--hero{left:100px;top:391px;width:119px;height:37px;font-size:12px}

  .band{left:0;top:527px;width:876px;height:323px;background:var(--red)}
  .card{position:absolute;top:561px;width:245px;height:249px;background:var(--white);border-radius:4px}
  .card h3{position:absolute;left:18px;top:7px;font-size:14px;font-weight:600}
  .card__img{position:absolute;left:18px;width:86px;height:66px}
  .card__txt{position:absolute;left:115px;width:125px;font-size:12px;line-height:9.2px;padding-top:3px}
  .btn--card{position:absolute;left:115px;top:200px;width:105px;height:28px;font-size:10px}

  .section-title{left:0;top:885px;width:876px;text-align:center;font-size:19.5px;font-weight:700}
  .feature{position:absolute;top:934px;width:120px;text-align:center;font-size:10.5px;font-weight:600;line-height:17px}
  .feature svg{display:block;margin:0 auto 8px;width:48px;height:54px}
  .btn--cta{left:368px;top:1060px;width:119px;height:37px;font-size:12px}

  .footer{left:0;top:1152px;width:876px;height:48px;background:var(--footer);color:#d9dbe3;font-size:8.5px}
  .footer__nav{position:absolute;left:96px;top:16px;display:flex;gap:20px}
  .footer__copy{position:absolute;right:96px;top:18px}
</style>
</head>
<body>
  <div class="blob blob--peach"></div>
  <div class="blob blob--apricot"></div>

  <header>
    <div class="abs brand"><span class="brand__dot"></span><span class="brand__name">falvoria.com</span></div>
    <nav class="abs nav"><span>Start</span><span>Services</span><span>Funktionen</span><span>Preise</span></nav>
    <div class="abs btn btn--head">Kostenlos testen</div>
    <div class="abs btn btn--ghost">Mein Falvoria</div>
  </header>

  <section class="hero">
    <div class="abs hero__photo" role="img" aria-label="Handwerker in der Werkstatt arbeitet lächelnd am Laptop"></div>
    <h1 class="abs hero__title">Marketing und<br>Recruiting<br>Services für<br>Handwerker.</h1>
    <div class="abs hero__text">
      <p>Wir gestalten das Handwerk von morgen - mit digitalen Losugen für Deine Betriebsführung.</p>
      <p>Werde online sichtbar und positioniere Dich als erfolgreicher Betrieb und Attaktiver Arbeitgeber.</p>
    </div>
    <div class="abs btn btn--hero">Kostenlos testen</div>
    <div class="blob blob--cyan"></div>
  </section>

  <section>
    <div class="abs band"></div>

    <article class="card" style="left:30px">
      <h3>Branchen-News</h3>
      <div class="card__img" style="top:41px;background:linear-gradient(160deg,#7fa6d4,#2c3f63 60%,#e0a52a)" role="img" aria-label="Industriegebäude mit gelber Fassade"></div>
      <p class="card__txt" style="top:41px">Lorem ipsum dolor sit amet, consectetur adipiscing elit. Pellentesque mattis venenatis mi varius condimentum.</p>
      <div class="card__img" style="top:125px;background:linear-gradient(160deg,#c9ced6,#6e7682)" role="img" aria-label="Rohrleitungen in einer Industrieanlage"></div>
      <p class="card__txt" style="top:124px">Lorem ipsum dolor sit amet, consectetur adipiscing elit. Pellentesque mattis venenatis mi varius condimentum.</p>
      <div class="btn btn--card">Zur Übersicht</div>
    </article>

    <article class="card" style="left:315px">
      <h3>Fortbildungen</h3>
      <div class="card__img" style="top:41px;background:linear-gradient(160deg,#3d8c86,#6fc0b4 50%,#1f3a38)" role="img" aria-label="Vortragender vor einer Projektion"></div>
      <p class="card__txt" style="top:41px">Lorem ipsum dolor sit amet, consectetur adipiscing elit. Pellentesque mattis venenatis mi varius condimentum.</p>
      <div class="card__img" style="top:125px;background:linear-gradient(160deg,#d8d8d8,#4a4a4a)" role="img" aria-label="Seminar, Teilnehmer melden sich, schwarz-weiß"></div>
      <p class="card__txt" style="top:124px">Lorem ipsum dolor sit amet, consectetur adipiscing elit. Pellentesque mattis venenatis mi varius condimentum.</p>
      <div class="btn btn--card">Zur Übersicht</div>
    </article>

    <article class="card" style="left:601px">
      <h3 style="top:9px">Jobs</h3>
      <div class="card__img" style="top:41px;background:linear-gradient(160deg,#4a5a88,#2b3450 55%,#b88a3a)" role="img" aria-label="Auszubildende beim Metallschleifen"></div>
      <p class="card__txt" style="top:41px">Lorem ipsum dolor sit amet, consectetur adipiscing elit. Pellentesque mattis venenatis mi varius condimentum.</p>
      <div class="card__img" style="top:125px;background:linear-gradient(160deg,#5a4a40,#8a6a3a 50%,#3a3a40)" role="img" aria-label="Elektriker mit Helm am Schaltschrank"></div>
      <p class="card__txt" style="top:124px">Lorem ipsum dolor sit amet, consectetur adipiscing elit. Pellentesque mattis venenatis mi varius condimentum.</p>
      <div class="btn btn--card">Zur Übersicht</div>
    </article>
  </section>

  <section>
    <h2 class="abs section-title">Wir machen Dich fit für die digtiale Betriebsführung</h2>

    <div class="feature" style="left:56px;top:932px">
      <svg viewBox="0 0 48 54"><circle cx="24" cy="24" r="24" fill="#f2f2f2"/><rect x="7" y="7" width="34" height="34" rx="5" fill="var(--red)"/><rect x="12" y="13" width="8" height="9" fill="#fff"/><rect x="12" y="26" width="8" height="9" fill="#fff"/><rect x="24" y="13" width="12" height="3" fill="#fff"/><rect x="24" y="19" width="12" height="3" fill="#fff"/><rect x="24" y="26" width="12" height="3" fill="#fff"/><rect x="24" y="32" width="12" height="3" fill="#fff"/></svg>
      Branchen-News<br>erhalten
    </div>
    <div class="feature" style="left:206px;top:935px">
      <svg viewBox="0 0 48 54"><rect x="17" y="5" width="14" height="8" rx="2" fill="none" stroke="var(--red)" stroke-width="3"/><rect x="5" y="12" width="38" height="26" rx="3" fill="var(--red)"/><rect x="12" y="17" width="3" height="16" fill="#fff"/><rect x="33" y="17" width="3" height="16" fill="#fff"/><rect x="3" y="41" width="42" height="2" fill="var(--red)"/></svg>
      Fachpersonal<br>finden
    </div>
    <div class="feature" style="left:367px;top:933px">
      <svg viewBox="0 0 48 54"><path d="M17 5h14v13h13v14H31v13H17V32H4V18h13z" fill="var(--red)"/></svg>
      Kunden<br>gewinnen
    </div>
    <div class="feature" style="left:539px;top:935px">
      <svg viewBox="0 0 48 54"><path d="M24 44C10 34 3 27 3 18 3 11 8 6 14 6c5 0 8 3 10 6 2-3 5-6 10-6 6 0 11 5 11 12 0 9-7 16-21 26z" fill="var(--red)"/></svg>
      Kundenbeziehung<br>stärken
    </div>
    <div class="feature" style="left:712px;top:935px">
      <svg viewBox="0 0 48 54"><circle cx="24" cy="22" r="21" fill="var(--red)"/><path d="M29 9c6 7 6 19 0 26" fill="none" stroke="#fff" stroke-width="2.5"/></svg>
      Betrieb<br>digitalisieren
    </div>

    <div class="abs btn btn--cta">Kostenlos testen</div>
  </section>

  <footer class="abs footer">
    <nav class="footer__nav"><span>Start</span><span>Services</span><span>Funktionen</span><span>Preise</span></nav>
    <span class="footer__copy">© 2022 Falvoria. All rights reserved</span>
  </footer>
</body>
</html>
```